They say laughter is the best medicine

This poster is for a nursing pharmacology class room with 70+students. Size is 24" x36". It needs to be a clean design. Would like vintage advertisement banners and script fonts. Would like a black background with an accent color. Please view pictures on word doc for examples.

```html
<!DOCTYPE html>
<html lang="en">
<head>
<meta charset="utf-8">
<title>They Say Laughter Is the Best Medicine – Poster</title>
<link href="https://fonts.googleapis.com/css2?family=Rye&family=Lobster&family=Great+Vibes&family=Dancing+Script:wght@400;600&family=Sacramento&family=Alfa+Slab+One&family=Tinos&family=Oswald:wght@400&display=swap" rel="stylesheet">
<style>
  :root {
    --backdrop-light: #8a919b;
    --backdrop-dark: #3f444b;
    --board: #262626;
    --board-glow: #353535;
    --chalk: #f2f2f2;
    --chalk-soft: #cfcfcf;
    --chalk-grey: #8d8d8d;
    --ink: #2b2b2b;
    --ribbon: #e6e6e6;
    --ribbon-shade: #9a9a9a;
  }
  * { margin: 0; padding: 0; box-sizing: border-box; }
  html, body { width: 1200px; height: 800px; overflow: hidden; }
  body {
    background: radial-gradient(ellipse at 30% 40%, var(--backdrop-light), var(--backdrop-dark) 75%);
    position: relative;
  }
  .poster {
    position: absolute;
    left: 340px; top: 10px;
    width: 520px; height: 780px;
    background: radial-gradient(ellipse at 50% 40%, var(--board-glow), var(--board) 80%);
    box-shadow: 0 6px 18px rgba(0,0,0,.35);
    color: var(--chalk);
    text-align: center;
  }
  .poster > *, .headline > * { position: absolute; white-space: nowrap; }

  .quote-mark { font-family: "Rye", serif; font-size: 44px; color: var(--chalk-soft); line-height: 1; }
  .quote-mark--open { left: 24px; top: 72px; }
  .quote-mark--close { right: 18px; top: 120px; }

  .headline { top: 0; left: 0; width: 520px; height: 290px; font-weight: normal; }
  .headline-intro {
    font-family: "Dancing Script", cursive; font-weight: 600;
    font-size: 46px; line-height: 1; top: 44px; left: 0; width: 100%; padding-left: 40px;
  }
  .headline-main {
    font-family: "Rye", serif; font-size: 66px; line-height: 1; letter-spacing: 1px;
    color: var(--chalk-grey);
    -webkit-text-stroke: 1.5px var(--chalk);
    text-shadow: 4px 4px 0 #1a1a1a;
    top: 108px; left: 0; width: 100%;
  }
  .headline-joiner {
    font-family: "Oswald", sans-serif; font-size: 18px; line-height: 1; letter-spacing: 3px;
    color: var(--chalk-soft); top: 188px; left: 320px;
  }

  .banner {
    background: linear-gradient(180deg, var(--ribbon), var(--ribbon-shade));
    border-radius: 6px;
  }
  .banner--headline { top: 212px; left: 150px; width: 220px; height: 60px; }
  .banner-text {
    font-family: "Dancing Script", cursive; color: var(--ink); font-weight: 600; line-height: 1;
  }
  .banner-text--best { top: 217px; left: 0; width: 100%; font-size: 22px; }
  .banner-text--medicine { top: 244px; left: 0; width: 100%; font-size: 18px; letter-spacing: 2px; }

  .subhead {
    font-family: "Lobster", cursive; font-size: 44px; line-height: 1; font-weight: normal;
    color: #d9d9d9; text-shadow: 2px 2px 0 #111;
    top: 288px; left: 0; width: 100%;
  }

  .drug-list {
    font-family: "Sacramento", cursive; font-size: 28px; line-height: 36px;
    color: var(--chalk); list-style: none; top: 350px;
  }
  .drug-list--left { left: 22px; width: 160px; text-align: left; }
  .drug-list--middle { left: 185px; width: 150px; text-align: center; }
  .drug-list--right { left: 348px; width: 160px; text-align: left; }

  .divider {
    top: 512px; left: 40px; width: 440px;
    border: 0; border-top: 2px dotted var(--chalk-soft);
  }
  .tagline {
    font-family: "Great Vibes", cursive; font-size: 36px; line-height: 40px; word-spacing: 6px;
    top: 526px; left: 0; width: 100%;
  }

  .banner--course { top: 622px; left: 100px; width: 320px; height: 40px; }
  .banner-text--course { top: 630px; left: 0; width: 100%; font-size: 22px; }

  .author-name {
    font-family: "Alfa Slab One", serif; font-size: 28px; line-height: 1; letter-spacing: 2px;
    top: 678px; left: 0; width: 100%;
  }
  .author-credentials {
    font-family: "Tinos", serif; font-size: 18px; line-height: 22px;
    color: var(--chalk-soft); top: 716px; left: 0; width: 100%;
  }
</style>
</head>
<body>
  <main class="poster">
    <span class="quote-mark quote-mark--open">“</span>
    <span class="quote-mark quote-mark--close">”</span>

    <h1 class="headline">
      <span class="headline-intro">They Say</span>
      <span class="headline-main">LAUGHTER</span>
      <span class="headline-joiner">IS THE</span>
    </h1>

    <div class="banner banner--headline" role="img" aria-label="Vintage scroll ribbon banner"></div>
    <span class="banner-text banner-text--best">BEST</span>
    <span class="banner-text banner-text--medicine">MEDICINE</span>

    <h2 class="subhead">- Well, We Think -</h2>

    <ul class="drug-list drug-list--left">
      <li>Acetaminophen</li>
      <li>Lorazepam</li>
      <li>MSO 4</li>
      <li>Furosemide</li>
    </ul>
    <ul class="drug-list drug-list--middle">
      <li>Vancomycin</li>
      <li>Insulin</li>
      <li>&amp;</li>
      <li>Oxygen</li>
    </ul>
    <ul class="drug-list drug-list--right">
      <li>Nitroglycerin</li>
      <li>Haloperidol</li>
      <li>Loperamide</li>
      <li>Albuterol</li>
    </ul>

    <hr class="divider">

    <p class="tagline">Just Might Be What You Want<br>More in Certain Situations</p>

    <div class="banner banner--course" role="img" aria-label="Vintage scroll ribbon banner"></div>
    <span class="banner-text banner-text--course">Nursing Pharmacology Concepts</span>

    <p class="author-name">EVELYN MARSH,</p>
    <p class="author-credentials">PhD, MSN, RN, CCRN, CPN, CNE<br>Clinical Professor</p>
  </main>
</body>
</html>
```